Business card and e-mail signature template.

I need a business card- and e-mail signature template for a project (signature will be used with gmail). The logo is attached.

There the logo has a focus on the “Lumora” part of the name. The URL for the project is www.lumorafest.com.
The full name of the project is The Lumora Expo. The project will be publicly known as “Lumora” or “Lumora2020”. In all documents we will present the project as Lumora2020.

The logo can contain design elements and the design should be modern and appealing to both young people and traditional companies.

This competition is part of a bigger delivery. The winner will therefore be a strong candidate for the brand guide og maybe website.

```html
<!DOCTYPE html>
<html lang="en">
<head>
<meta charset="utf-8">
<title>Lumora2020 Business Card</title>
<link href="https://fonts.googleapis.com/css2?family=Montserrat:wght@400;500;600;700&display=swap" rel="stylesheet">
<style>
  :root {
    --page-bg: #ececec;
    --card-white: #ffffff;
    --brand-orange: #ee8a3c;
    --brand-pink: #e5487a;
    --brand-magenta: #d63a78;
    --ink-dark: #3a3a3a;
    --ink-muted: #6b6b6b;
    --frame-white: rgba(255,255,255,0.9);
  }
  * { box-sizing: border-box; margin: 0; padding: 0; }
  html, body {
    width: 1200px; height: 799px; overflow: hidden;
    background: var(--page-bg);
    font-family: "Montserrat", sans-serif;
  }
  .canvas {
    position: relative; width: 1200px; height: 799px;
  }
  .card {
    position: absolute; top: 260px;
    width: 500px; height: 280px;
    box-shadow: 0 14px 30px rgba(0,0,0,0.12);
  }
  /* Front side */
  .card--front {
    left: 70px;
    background: linear-gradient(30deg, var(--brand-orange) 0%, #ec7554 45%, var(--brand-pink) 100%);
  }
  .card--front .card__frame {
    position: absolute; inset: 14px;
    border: 1.5px solid var(--frame-white);
  }
  .front-mark {
    position: absolute; left: 0; right: 0; top: 0; bottom: 0;
    display: flex; align-items: center; justify-content: center; gap: 16px;
  }
  .front-mark__dot {
    width: 30px; height: 30px; border-radius: 50%;
    background: var(--card-white);
  }
  .front-mark__name {
    color: var(--card-white);
    font-weight: 600; font-size: 38px; letter-spacing: 1px;
  }
  /* Back side */
  .card--back {
    left: 630px;
    background: var(--card-white);
  }
  .card--back .card__frame {
    position: absolute; inset: 14px;
    border: 2px solid var(--brand-orange);
  }
  .contact {
    position: absolute; left: 40px; top: 36px;
  }
  .contact__name {
    color: var(--brand-orange);
    font-weight: 600; font-size: 17px; letter-spacing: 0.5px;
    text-transform: uppercase;
  }
  .contact__role {
    color: var(--ink-dark);
    font-weight: 700; font-size: 13px; letter-spacing: 0.5px;
    margin-top: 2px;
  }
  .contact__address {
    color: var(--ink-muted);
    font-size: 10px; line-height: 1.45; margin-top: 10px;
  }
  .contact__rule {
    width: 110px; height: 1px; background: var(--brand-orange);
    margin: 10px 0 12px;
  }
  .contact__list { list-style: none; }
  .contact__item {
    display: flex; align-items: center; gap: 9px;
    color: var(--ink-muted); font-size: 10.5px;
    margin-bottom: 7px;
  }
  .contact__item svg { width: 11px; height: 11px; flex: none; }
  .back-mark {
    position: absolute; right: 42px; bottom: 44px;
    display: flex; align-items: center; gap: 12px;
  }
  .back-mark__dot {
    width: 22px; height: 22px; border-radius: 50%;
    background: var(--brand-magenta);
  }
  .back-mark__name {
    color: var(--brand-magenta);
    font-weight: 600; font-size: 30px; letter-spacing: 1px;
  }
</style>
</head>
<body>
<main class="canvas">

  <section class="card card--front" aria-label="Card front">
    <div class="card__frame"></div>
    <div class="front-mark">
      <span class="front-mark__dot"></span>
      <span class="front-mark__name">Lumora2020</span>
    </div>
  </section>

  <section class="card card--back" aria-label="Card back">
    <div class="card__frame"></div>
    <div class="contact">
      <p class="contact__name">Jonas Berg</p>
      <p class="contact__role">FOUNDER</p>
      <p class="contact__address">1180 Harbor Lane 12<br>Westbrook Park</p>
      <div class="contact__rule"></div>
      <ul class="contact__list">
        <li class="contact__item">
          <svg viewBox="0 0 24 24" fill="var(--brand-orange)"><path d="M6.6 10.8a15.1 15.1 0 0 0 6.6 6.6l2.2-2.2a1 1 0 0 1 1-.25 11.4 11.4 0 0 0 3.6.57 1 1 0 0 1 1 1V20a1 1 0 0 1-1 1A17 17 0 0 1 3 4a1 1 0 0 1 1-1h3.5a1 1 0 0 1 1 1c0 1.25.2 2.45.57 3.57a1 1 0 0 1-.25 1z"/></svg>
          000-000-000
        </li>
        <li class="contact__item">
          <svg viewBox="0 0 24 24" fill="none" stroke="var(--brand-orange)" stroke-width="2.2"><circle cx="12" cy="12" r="9"/><path d="M3 12h18M12 3c3 3.5 3 14.5 0 18M12 3c-3 3.5-3 14.5 0 18"/></svg>
          www.lumorafest.com
        </li>
        <li class="contact__item">
          <svg viewBox="0 0 24 24" fill="none" stroke="var(--brand-orange)" stroke-width="2.2"><rect x="3" y="5" width="18" height="14" rx="1.5"/><path d="M3 6l9 7 9-7"/></svg>
          info@lumorafest.com
        </li>
      </ul>
    </div>
    <div class="back-mark">
      <span class="back-mark__dot"></span>
      <span class="back-mark__name">Lumora2020</span>
    </div>
  </section>

</main>
</body>
</html>
```